Job advert for Forged Here Collective

I would like a poster graphic that I can promote on social media to advertise a job vacancy we will be promoting our upcoming jobs, here is the text...

WE ARE ON THE…

LOOKOUT
(maybe insert graphic or icon that fits with the message here)

For A

OPERATIONS AND HR MANAGER

MEMBERSHIP ADVISOR (EAST MIDLANDS)

SOCIAL MEDIA CONTENT CREATOR

THE UK’s FASTEST GROWING NETWORK FOR MANUFACTURERS

OFFICES IN BIRMINGHAM AND LEEDS - WE ARE AN INCLUSIVE EMPLOYER (use the equality logo provided here)

Target Market(s)

people looking to find a new job

Industry/Entity Type

Manufacture

Font styles to use
Sans Serif

Colors
f04a50
f68e4e
e667a6

Requirements
Must have
• Clear simple and contemporary style
Nice to have
• a nice graphic or icon to convey the text message
Should not have
• use of dark depressing colours

```html
<!DOCTYPE html>
<html lang="en">
<head>
<meta charset="utf-8">
<title>Forged Here Collective – We Are On The Lookout</title>
<link href="https://fonts.googleapis.com/css2?family=Roboto:ital,wght@0,300;0,400;0,500;0,700;1,300;1,700;1,900&display=swap" rel="stylesheet">
<style>
  :root {
    --sky-top: #243556;
    --sky-mid: #7f9cc4;
    --sky-light: #c9d8ea;
    --navy: #0f1a33;
    --heading-navy: #17294f;
    --ink: #0d1524;
    --grey-ink: #2a3140;
    --badge-grey: #d3d7de;
    --yellow: #f2ea2a;
    --lime: #a6cc2f;
    --white: #ffffff;
  }
  * { margin: 0; padding: 0; box-sizing: border-box; }
  html, body { width: 1200px; height: 654px; overflow: hidden; background: var(--navy); }
  body { font-family: "Roboto", Arial, sans-serif; }

  .poster { position: relative; width: 1200px; height: 654px; overflow: hidden; }

  .backdrop {
    position: absolute; inset: 0;
    background:
      radial-gradient(ellipse 520px 300px at 640px 300px, var(--sky-light) 0%, rgba(201,216,234,0) 100%),
      linear-gradient(180deg, var(--sky-top) 0%, var(--sky-mid) 45%, #6f8bb3 75%, var(--sky-top) 100%);
  }

  .text { position: absolute; white-space: nowrap; line-height: 1; }

  .lead { left: 77px; top: 92px; font-size: 56px; font-weight: 300; color: var(--yellow); letter-spacing: 0.5px; }
  .lookout { left: 536px; top: 39px; font-size: 120px; font-weight: 400; color: var(--lime); letter-spacing: 3px;
             text-shadow: 4px 4px 3px rgba(0,0,0,0.55); }

  .tagline-band { position: absolute; left: 538px; top: 147px; width: 662px; height: 68px; background: var(--navy); }
  .tagline { left: 561px; top: 153px; font-size: 24px; font-weight: 300; color: var(--white); line-height: 28px; }
  .tagline strong { font-weight: 700; }
  .tagline em { font-weight: 700; font-style: italic; }

  .role-light { font-weight: 300; font-style: italic; color: var(--ink); }
  .role-bold { font-weight: 900; font-style: italic; color: var(--ink); }
  .operations { left: 380px; top: 240px; font-size: 38px; }
  .hr-manager { left: 477px; top: 279px; font-size: 55px; }
  .membership { left: 539px; top: 351px; font-size: 47px; color: var(--heading-navy); }
  .region { left: 672px; top: 398px; font-size: 29.5px; font-weight: 700; color: var(--grey-ink); }
  .social { left: 494px; top: 426px; font-size: 35px; }
  .creator { left: 494px; top: 465px; font-size: 35px; }

  .footer-band { position: absolute; left: 0; top: 558px; width: 1200px; height: 56px; }
  .footer-text { left: 66px; top: 578px; font-size: 18px; font-weight: 400; color: var(--white); letter-spacing: 0.4px; }

  .partner-badge { position: absolute; top: 570px; height: 32px; border-radius: 16px; background: var(--badge-grey); }
  .partner-badge.first { left: 795px; width: 104px; }
  .partner-badge.second { left: 940px; width: 92px; }
  .partner-badge.third { left: 1072px; width: 86px; }
</style>
</head>
<body>
<main class="poster">
  <div class="backdrop" role="img" aria-label="Photo of a businessman in a suit shouting through a megaphone against a cloudy blue sky, arm outstretched"></div>

  <div class="text lead">WE ARE ON THE…</div>
  <div class="text lookout">LOOKOUT</div>

  <div class="tagline-band"></div>
  <div class="text tagline"><strong>THE UK’s FASTEST</strong> GROWING NETWORK<br>FOR <em>MANUFACTURERS</em></div>

  <div class="text operations role-light">OPERATIONS</div>
  <div class="text hr-manager role-bold">HR MANAGER</div>
  <div class="text membership role-bold">MEMBERSHIP ADVISOR</div>
  <div class="text region">(EAST MIDLANDS)</div>
  <div class="text social role-light">SOCIAL MEDIA</div>
  <div class="text creator role-bold">CONTENT CREATOR</div>

  <svg class="footer-band" viewBox="0 0 1200 56" aria-hidden="true">
    <rect x="708" y="0" width="492" height="56" fill="#ffffff"/>
    <polygon points="0,0 708,0 740,28 708,56 0,56" fill="#0f1a33"/>
  </svg>
  <div class="text footer-text">OFFICES IN BIRMINGHAM AND LEEDS - WE ARE AN INCLUSIVE EMPLOYER</div>

  <div class="partner-badge first" role="img" aria-label="Inclusive employer pledge badge"></div>
  <div class="partner-badge second" role="img" aria-label="Regional network badge"></div>
  <div class="partner-badge third" role="img" aria-label="Regional network badge"></div>
</main>
</body>
</html>
```